Storm Restoration Contractor needs a professional business card design

Looking for a professional business card design. Not looking for your cheapo MS Word standard ones that are readily available. Dont want it to be cookie cutter look like ones readily available online. We just recently changed our logo and want to freshen up all our documents. Our company handles restoring a property back to a pre-loss condition after a storm damages it. For example, wind, hail, flood, fire losses.

Target Market(s)

Property Owners, Homeowners, Property Owners, Commercial Property Owners, Property Management Companies, Hail and Wind Damaged Properties

Industry/Entity Type

Construction Company

Contact Information for Business Card

Brightline Facades
847-555-0193
847-555-0147 fax
www.brightlinefacades.example
info@brightlinefacades.example

Requirements
Must have
• Clean, Professional, fresh look
• Storm Restoration, Roofing, Siding, Windows
Nice to have
• If there is a way to incorporate storms that may be cool.

```html
<!DOCTYPE html>
<html lang="en">
<head>
<meta charset="utf-8">
<title>Brightline Facades – Business Card</title>
<link rel="stylesheet" href="https://fonts.googleapis.com/css2?family=Roboto:ital,wght@0,400;0,500;0,700;1,700&display=swap">
<style>
  :root {
    --page-bg: #2b2b2d;
    --card-white: #ffffff;
    --card-mist: #eef2f6;
    --brand-blue: #1f72bd;
    --brand-blue-dark: #175c9c;
    --brand-grey: #5d5f63;
    --text-white: #ffffff;
    --storm-light: #d8eaf8;
    --storm-mid: #8cc3ea;
  }
  * { box-sizing: border-box; margin: 0; padding: 0; }
  html, body { width: 1200px; height: 997px; overflow: hidden; }
  body {
    background: var(--page-bg);
    font-family: "Roboto", Arial, sans-serif;
    position: relative;
  }
  .card {
    position: absolute;
    width: 540px;
    height: 310px;
    border-radius: 18px;
    overflow: hidden;
    box-shadow: 0 12px 30px rgba(0,0,0,.45);
  }

  /* ---- Contact side ---- */
  .card--contact {
    left: 80px; top: 110px;
    background: var(--card-white);
  }
  .contact__brand {
    position: absolute; left: 150px; top: 52px;
    display: flex; align-items: center; gap: 12px;
  }
  .brand__dot {
    width: 34px; height: 34px; border-radius: 50%;
    background: var(--brand-blue);
  }
  .brand__name {
    font-weight: 700; font-size: 26px; letter-spacing: .5px;
    color: var(--brand-blue); text-transform: uppercase; line-height: 1;
  }
  .contact__rule {
    position: absolute; left: 0; right: 0; top: 132px;
    height: 4px; background: var(--brand-blue);
  }
  .contact__band {
    position: absolute; left: 0; right: 0; top: 142px; bottom: 0;
    background: linear-gradient(180deg, var(--brand-blue) 0%, var(--brand-blue-dark) 100%);
    color: var(--text-white);
  }
  .band__marker {
    position: absolute; left: 28px; top: 0;
    width: 0; height: 0;
    border-left: 7px solid transparent; border-right: 7px solid transparent;
    border-top: 8px solid var(--card-white);
  }
  .person { position: absolute; left: 28px; top: 16px; }
  .person__name { font-size: 21px; font-weight: 400; }
  .person__title { font-size: 12px; opacity: .9; margin-top: 2px; }
  .contact__list {
    position: absolute; left: 28px; top: 76px;
    list-style: none; font-size: 13px;
  }
  .contact__list li { display: flex; align-items: center; gap: 9px; margin-bottom: 7px; }
  .contact__list svg { width: 16px; height: 16px; flex: none; }
  .company-address {
    position: absolute; right: 26px; top: 18px;
    text-align: right; font-size: 11px; line-height: 1.45;
  }
  .company-address strong { font-weight: 500; }

  /* ---- Brand side ---- */
  .card--brand {
    left: 580px; top: 530px;
    background: linear-gradient(180deg, var(--card-white) 0%, var(--card-mist) 100%);
  }
  .storm-art {
    position: absolute; left: 40px; top: 0; width: 250px; height: 310px;
    background: radial-gradient(ellipse at 55% 40%, var(--storm-mid) 0%, var(--storm-light) 45%, rgba(255,255,255,0) 75%);
  }
  .brand-front {
    position: absolute; left: 150px; top: 112px;
    display: flex; align-items: center; gap: 14px;
  }
  .brand-front .brand__dot { width: 44px; height: 44px; }
  .brand-front .brand__name { font-size: 32px; }
  .services {
    position: absolute; left: 150px; top: 178px;
    font-size: 14px; font-weight: 700; font-style: italic;
    color: var(--brand-blue);
  }
</style>
</head>
<body>

<section class="card card--contact" aria-label="Business card, contact side">
  <div class="contact__brand">
    <span class="brand__dot"></span>
    <span class="brand__name">Brightline Facades</span>
  </div>
  <div class="contact__rule"></div>
  <div class="contact__band">
    <span class="band__marker"></span>
    <div class="person">
      <p class="person__name">Dana Keller</p>
      <p class="person__title">Licensed Electrician</p>
    </div>
    <ul class="contact__list">
      <li>
        <svg viewBox="0 0 16 16" aria-hidden="true"><rect width="16" height="16" rx="3" fill="#fff"/><path d="M5 4l2 2-1 1.2a6 6 0 0 0 2.8 2.8L10 9l2 2-1.2 1.3C7.5 12 4 8.5 3.7 5.2z" fill="#1f72bd"/></svg>
        847-555-0193
      </li>
      <li>
        <svg viewBox="0 0 16 16" aria-hidden="true"><rect width="16" height="16" rx="3" fill="#fff"/><rect x="4" y="6" width="8" height="5" fill="#1f72bd"/><rect x="5.5" y="3.5" width="5" height="3" fill="none" stroke="#1f72bd"/></svg>
        847-555-0147
      </li>
      <li>
        <svg viewBox="0 0 16 16" aria-hidden="true"><rect width="16" height="16" rx="3" fill="#fff"/><rect x="3.5" y="5" width="9" height="6.5" fill="none" stroke="#1f72bd"/><path d="M3.5 5l4.5 3.5L12.5 5" fill="none" stroke="#1f72bd"/></svg>
        info@brightlinefacades.example
      </li>
    </ul>
    <p class="company-address"><strong>Brightline Facades Pvt. Ltd.</strong><br>22 Harbor Lane, Millbrook 4021</p>
  </div>
</section>

<section class="card card--brand" aria-label="Business card, brand side">
  <div class="storm-art" role="img" aria-label="Pale blue tornado and storm photograph fading into white"></div>
  <div class="brand-front">
    <span class="brand__dot"></span>
    <span class="brand__name">Brightline Facades</span>
  </div>
  <p class="services">Storm Restoration • Roofing • Siding Windows</p>
</section>

</body>
</html>
```